Music Artist Needs Flyer Design ASAP

Looking for a flyer design to promote for artist release party. Music artist is mainly hip hop based. We would like designs that are simple, creative and eye catching.

Requirements
Must have
• The flyer must have the photo of the artist I attached incorporated into the design. Must say "Free ZUKO" Release Party, Live at Tolly's Bar Thursday Dec.27 2012 (artist name=ZUKO VeN), show starts at 8pm, No cover charge, 21 and over, Register to Win Coral Blaze tickets Giveaway

```html
<!DOCTYPE html>
<html lang="en">
<head>
<meta charset="utf-8">
<title>Free ZUKO Release Party</title>
<link href="https://fonts.googleapis.com/css2?family=Arimo:wght@700&display=swap" rel="stylesheet">
<style>
  :root {
    --ink: #000000;
    --paper: #ffffff;
    --gold: #fbbf24;
    --photo-hi: #f5d21c;
    --photo-mid: #e8a416;
    --photo-low: #9c3a0e;
  }
  * { margin: 0; padding: 0; box-sizing: border-box; }
  html, body { width: 872px; height: 1200px; overflow: hidden; background: var(--ink); }
  .flyer {
    position: relative; width: 872px; height: 1200px; overflow: hidden;
    background: var(--ink); color: var(--paper);
    font-family: "Arimo", Arial, sans-serif; font-weight: 700;
  }
  .headline {
    position: absolute; left: 0; right: 0; top: 4px;
    text-align: center; font-size: 134px; line-height: 1; letter-spacing: -1px;
  }
  .artist-photo {
    position: absolute; left: 74px; top: 138px; width: 532px; height: 738px;
    background:
      radial-gradient(ellipse at 30% 20%, var(--photo-low) 0%, transparent 45%),
      radial-gradient(ellipse at 40% 70%, var(--photo-hi) 0%, transparent 60%),
      linear-gradient(160deg, var(--photo-mid), var(--photo-hi) 55%, var(--photo-mid));
  }
  .tag {
    position: absolute; background: var(--ink); text-align: center; line-height: 1.05;
  }
  .tag--release { left: 390px; top: 142px; width: 412px; height: 62px; font-size: 42px; padding-top: 8px; }
  .tag--venue { left: 426px; top: 220px; width: 382px; height: 152px; font-size: 66px; padding-top: 6px; }
  .tag--artist { left: 366px; top: 386px; width: 436px; height: 146px; padding-top: 8px; }
  .tag--artist .label { font-size: 44px; display: block; }
  .tag--artist .name { font-size: 64px; display: block; margin-top: 4px; }
  .date {
    position: absolute; left: 564px; top: 540px; width: 252px; height: 336px;
    background: var(--ink); text-align: center; line-height: 1;
  }
  .date .weekday { display: block; font-size: 42px; margin-top: 8px; }
  .date .month { display: block; font-size: 72px; margin-top: 6px; }
  .date .day { display: block; font-size: 150px; margin-top: -4px; letter-spacing: -4px; }
  .date .year { display: block; font-size: 54px; margin-top: -4px; }
  .showtime {
    position: absolute; left: 0; right: 0; top: 884px;
    text-align: center; font-size: 60px; line-height: 1;
  }
  .age-band {
    position: absolute; left: 74px; top: 972px; width: 732px; height: 72px;
    background: var(--gold);
  }
  .age-band::before {
    content: ""; position: absolute; left: 0; right: 0; top: 34px; height: 5px; background: var(--ink);
  }
  .age-band .age {
    position: absolute; left: 50%; top: 0; transform: translateX(-50%);
    background: var(--gold); color: var(--ink); font-size: 54px; line-height: 72px; padding: 0 8px;
  }
  .cover {
    position: absolute; left: 74px; top: 1044px; width: 208px; height: 130px;
    background: var(--gold); color: var(--ink);
    border-radius: 0 0 104px 104px / 0 0 100px 100px;
    text-align: center; font-size: 34px; line-height: 1.1; padding-top: 12px;
  }
  .giveaway {
    position: absolute; left: 350px; top: 1082px; width: 480px;
    text-align: center; font-size: 27px; line-height: 1.3;
  }
</style>
</head>
<body>
<main class="flyer">
  <h1 class="headline">Free ZUKO</h1>
  <div class="artist-photo" role="img" aria-label="Photo of the artist ZUKO VeN in a white t-shirt, warm yellow and orange tones"></div>
  <div class="tag tag--release">Release Party</div>
  <div class="tag tag--venue">Live at<br>Tolly's Bar</div>
  <div class="tag tag--artist"><span class="label">ARTIST NAME</span><span class="name">ZUKO VeN</span></div>
  <div class="date">
    <span class="weekday">Thursday</span>
    <span class="month">Dec</span>
    <span class="day">27</span>
    <span class="year">2012</span>
  </div>
  <p class="showtime">Show starts at 8pm</p>
  <div class="age-band"><span class="age">21 and over</span></div>
  <div class="cover">No cover<br>charge</div>
  <p class="giveaway">Register to Win<br>Coral Blaze tickets Giveaway</p>
</main>
</body>
</html>
```